Buchverlag sucht Cover-Design
Zielgruppe
Wir sind ein Buchverlag, der über Bravolo publizieren.
Unsere Zielgruppe sind: alle Selbstständigen, Unternehmern, Intrapreneuren, genauso wie Coaches, Experten, Start-ups und Entrepreneure.
Auch an diejenigen, die dieses Vorhaben angehen möchten.
Aufgabenstellung
Das Cover soll Nischen entsprechend sein. (Business Findung und Gestaltung)
Andersartig, auffallend, jedoch seriös sein.
Genaue Vorstellung:
Ein im freien Naturlandschaft fliegender Adler, der seine Beute fest im Blick hat und zielgenau seine Beute
zugreifen kann!
Den Schriftzug auffällig gestalten
Titel:
HOHE WARTE - Echter Reichtum gehört jedem von Anfang an
Untertitel:
Die klare Haltung der Vorreiter mit praktischem Wegweiser für Klarheit & Zufriedenheit bei privaten und beruflichen Weichenstellungen
Autor:
Velina Korbach
Logo des Verlags im Anhang
Name des Verlags:
Mond Quelle Verlag

```html
<!DOCTYPE html>
<html lang="de">
<head>
<meta charset="utf-8">
<title>HOHE WARTE – Velina Korbach</title>
<link rel="stylesheet" href="https://fonts.googleapis.com/css2?family=Open+Sans:wght@600&family=Playfair+Display:wght@400&display=swap">
<style>
  :root {
    --sky-top: #3f7fb8;
    --sky-mid: #8db8d4;
    --sky-pale: #d7e0e2;
    --horizon-glow: #f4e6cd;
    --dawn-peach: #e8b998;
    --mist-rose: #cfa893;
    --mist-low: #a99a92;
    --accent-gold: #f8b938;
    --text-white: #ffffff;
  }
  html, body {
    margin: 0;
    padding: 0;
    width: 848px;
    height: 1200px;
    overflow: hidden;
    background: #ffffff;
  }
  .cover {
    position: relative;
    width: 848px;
    height: 1200px;
    overflow: hidden;
    font-family: "Open Sans", Arial, sans-serif;
    color: var(--text-white);
  }
  .cover-scene {
    position: absolute;
    inset: 0;
    background: linear-gradient(180deg,
      var(--sky-top) 0%,
      var(--sky-mid) 38%,
      var(--sky-pale) 58%,
      var(--horizon-glow) 68%,
      var(--dawn-peach) 72%,
      var(--mist-rose) 84%,
      var(--mist-low) 100%);
  }
  .author {
    position: absolute;
    left: 45px;
    top: 26px;
    margin: 0;
    font-size: 37px;
    font-weight: 600;
    color: var(--accent-gold);
    letter-spacing: 0.2px;
  }
  .title {
    position: absolute;
    left: 46px;
    top: 52px;
    margin: 0;
    font-family: "Playfair Display", Georgia, serif;
    font-weight: 400;
    font-size: 196px;
    line-height: 158px;
    letter-spacing: -3px;
    color: var(--text-white);
  }
  .title-line { display: block; }
  .subtitle {
    position: absolute;
    left: 52px;
    top: 404px;
    margin: 0;
    font-size: 31px;
    font-weight: 600;
    letter-spacing: -0.5px;
    white-space: nowrap;
  }
  .tagline {
    position: absolute;
    left: 52px;
    top: 862px;
    width: 640px;
    margin: 0;
    font-size: 25.5px;
    line-height: 41px;
    font-weight: 600;
    letter-spacing: -0.2px;
  }
  .publisher {
    position: absolute;
    left: 350px;
    top: 1120px;
    display: flex;
    align-items: center;
    gap: 10px;
  }
  .publisher-dot {
    width: 24px;
    height: 24px;
    border-radius: 50%;
    background: var(--accent-gold);
  }
  .publisher-name {
    font-size: 44px;
    font-weight: 600;
    color: var(--accent-gold);
    line-height: 1;
  }
</style>
</head>
<body>
  <main class="cover">
    <div class="cover-scene" role="img" aria-label="Fotografie: ein Greifvogel gleitet mit ausgebreiteten Flügeln über einer nebligen Berglandschaft im Sonnenaufgang unter blauem Himmel"></div>

    <p class="author">Velina Korbach</p>

    <h1 class="title">
      <span class="title-line">HOHE</span>
      <span class="title-line">WARTE</span>
    </h1>

    <p class="subtitle">Echter Reichtum gehört jedem von Anfang an</p>

    <p class="tagline">Die klare Haltung der Vorreiter mit praktischem Wegweiser für Klarheit &amp; Zufriedenheit bei privaten und beruflichen Weichenstellungen</p>

    <div class="publisher">
      <span class="publisher-dot"></span>
      <span class="publisher-name">MQV</span>
    </div>
  </main>
</body>
</html>
```